Calloway Law - New Letterhead/Logo

Hello!
THE FIRM NAME IS NOW CALLOWAY LAW. We recently just changed our name and we are in need of a classy letterhead. Attached I have a logo we have included in the past, but we are willing to look at other alternatives as well. I will also attach our current letterhead with our old name, Calloway & Associates. We are willing to go without attorney names. Please help! Thanks
Updates
Project Deadline Extended Reason: Haven't found anything we love Added Tuesday, November 1, 2016

```html
<!DOCTYPE html>
<html lang="en">
<head>
<meta charset="utf-8">
<title>Calloway Law Letterhead</title>
<link href="https://fonts.googleapis.com/css2?family=Source+Sans+3:wght@400&display=swap" rel="stylesheet">
<style>
  :root {
    --backdrop: #757575;
    --paper: #ffffff;
    --navy: #0c4a8c;
    --ink-blue: #1d4f95;
    --gold: #f6c063;
    --watermark: #e8eaf4;
    --footer-text: #ffffff;
  }
  * { margin: 0; padding: 0; box-sizing: border-box; }
  html, body {
    width: 1200px; height: 1200px; overflow: hidden;
    background: var(--backdrop);
    font-family: "Source Sans 3", "Myriad Pro", Arial, sans-serif;
  }
  .letterhead {
    position: absolute; left: 136px; top: 0;
    width: 928px; height: 1200px;
    background: var(--paper);
    overflow: hidden;
  }
  .firm-name {
    position: absolute; left: 0; right: 0; top: 52px; height: 90px;
    display: flex; justify-content: center; align-items: center; gap: 22px;
    color: var(--ink-blue);
    font-size: 72px; font-weight: 400; letter-spacing: 1px; line-height: 1;
    white-space: nowrap;
  }
  .firm-name .mark-square {
    width: 52px; height: 52px; background: var(--ink-blue); flex: none;
  }
  .attorneys {
    position: absolute; top: 170px; left: 0; right: 0;
    color: var(--ink-blue); font-size: 17px;
  }
  .attorneys li {
    position: absolute; list-style: none; white-space: nowrap;
  }
  .attorneys li::before { content: "\2022"; margin-right: 2px; }
  .attorneys li:nth-child(1) { left: 132px; }
  .attorneys li:nth-child(2) { left: 362px; }
  .attorneys li:nth-child(3) { left: 605px; }
  .header-rule {
    position: absolute; left: 0; right: 0; top: 209px; height: 8px;
    background: var(--gold);
  }
  .watermark-name {
    position: absolute; left: 0; right: 0; top: 560px;
    text-align: center; color: var(--watermark);
    font-size: 120px; font-weight: 400; line-height: 1; white-space: nowrap;
  }
  .footer-wave {
    position: absolute; left: 0; bottom: 0; width: 928px; height: 150px;
  }
  .contact {
    position: absolute; top: 1110px; left: 29px;
    color: var(--footer-text); font-size: 18px; line-height: 22px;
    display: grid; grid-template-columns: 110px auto;
  }
  .contact a { color: var(--gold); text-decoration: none; }
  .address {
    position: absolute; top: 1108px; right: 22px;
    color: var(--footer-text); font-size: 18px; line-height: 22.5px;
    text-align: right; font-style: normal;
  }
</style>
</head>
<body>
  <main class="letterhead">
    <header>
      <div class="firm-name"><span class="mark-square"></span><span>Calloway Law</span></div>
      <ul class="attorneys">
        <li>Marcus T. Calloway, Esq.</li>
        <li>Daniel P. Whitfield, Esq.</li>
        <li>Owen R. Castellano, Esq.</li>
      </ul>
      <div class="header-rule"></div>
    </header>

    <div class="watermark-name">Calloway Law</div>

    <footer>
      <svg class="footer-wave" viewBox="0 0 928 150" preserveAspectRatio="none" aria-hidden="true">
        <path d="M0 20 C 180 46, 320 48, 520 30 S 820 -2, 928 24 L 928 150 L 0 150 Z" fill="var(--gold)"/>
        <path d="M0 31 C 180 56, 320 56, 520 40 S 820 6, 928 32 L 928 150 L 0 150 Z" fill="var(--navy)"/>
      </svg>
      <div class="contact">
        <span>Phone</span><span>: (303) 555-0147</span>
        <span>Fax</span><span>: (303) 555-0162</span>
        <span>Web</span><span>: <a href="#">www.callowaylegal.net</a></span>
      </div>
      <address class="address">
        2810 Meridian Parkway<br>
        Suite 410 Aspen Grove<br>
        Colorado 80199
      </address>
    </footer>
  </main>
</body>
</html>
```